Collectible Fun Cards for Children

I have an idea of the type of card we want. Looking for an illustrator to help bring the idea to life very quickly. The cards will be in three series, with each series having a total of 36 cards each. I can supply most of the ideas for the cards but will need the successful designer to craft the cards in an attractive way. Ideally each car card will be of a different color. The preference will be for the two card images supplied to be merged. Of course, the successful candidate will be the one who is able to make come up with the best design, even better than the ones supplied.
I have added a hand-designed rendition of the card I have in mind for guidance.
The Purpose
• Engagement: Make kids excited to collect, trade, and read them.
• Education: Slip in simple but accurate nutrition, growth, and development facts.
• Branding: Position our brand as a premium, fun, and trustworthy product.

Target Market(s)

Children

Industry/Entity Type

Health and Wellness

Requirements
Must have
• Fun characters
Should not have
• Profanity. Incorrect information

```html
<!DOCTYPE html>
<html lang="en">
<head>
<meta charset="utf-8">
<title>Nutrition Series Collectible Cards</title>
<link href="https://fonts.googleapis.com/css2?family=Fira+Sans:wght@600&family=Ubuntu:wght@500;700&display=swap" rel="stylesheet">
<style>
  :root {
    --page-bg: #fef7e7;
    --frame: #e0d8c8;
    --cream-text: #ede2cf;
    --pill: #a7312a;
    --pill-text: #f6ecdb;
    --body-text: #1a0f08;
    --potato-top: #b94a25;
    --potato-bottom: #cf652a;
    --carrot-top: #cd652a;
    --carrot-bottom: #dd8a28;
    --mushroom-top: #2194a7;
    --mushroom-bottom: #107a86;
    --potato-light: #d8ab5c;
    --potato-dark: #a9803f;
    --carrot-leaf: #69ad58;
    --carrot-body: #ee6a2c;
    --mushroom-cap: #8a4723;
    --mushroom-stem: #d99c52;
  }
  * { box-sizing: border-box; margin: 0; padding: 0; }
  html, body { width: 1200px; height: 1200px; overflow: hidden; background: var(--page-bg); }
  .canvas { position: relative; width: 1200px; height: 1200px; }

  .card-frame {
    position: absolute;
    width: 321px;
    height: 481px;
    padding: 12px;
    border-radius: 26px;
    background: var(--frame);
    box-shadow: 10px 12px 14px rgba(40, 30, 20, 0.45);
  }
  .card-frame--potato { left: 76px; top: 345px; }
  .card-frame--carrot { left: 438px; top: 346px; }
  .card-frame--mushroom { left: 804px; top: 350px; }

  .card {
    position: relative;
    width: 100%;
    height: 100%;
    border-radius: 16px;
    overflow: hidden;
    background: var(--top);
    text-align: center;
  }
  .card--potato { --top: var(--potato-top); --bottom: var(--potato-bottom); }
  .card--carrot { --top: var(--carrot-top); --bottom: var(--carrot-bottom); }
  .card--mushroom { --top: var(--mushroom-top); --bottom: var(--mushroom-bottom); }

  .card__band {
    position: absolute;
    left: 0; right: 0; bottom: 0;
    height: 105px;
    background: var(--bottom);
  }
  .card__vitamin {
    position: absolute;
    top: 14px; left: 0; right: 0;
    font-family: "Ubuntu", sans-serif;
    font-weight: 700;
    font-size: 23px;
    line-height: 1;
    color: var(--cream-text);
  }
  .card__name {
    position: absolute;
    top: 39px; left: 0; right: 0;
    font-family: "Ubuntu", sans-serif;
    font-weight: 700;
    font-size: 37px;
    line-height: 1;
    color: var(--cream-text);
  }
  .card__character {
    position: absolute;
    left: 50%;
    top: 92px;
    width: 176px;
    height: 232px;
    transform: translateX(-50%);
    border-radius: 28px;
  }
  .card--potato .card__character { background: linear-gradient(160deg, var(--potato-light), var(--potato-dark)); }
  .card--carrot .card__character { background: linear-gradient(180deg, var(--carrot-leaf) 0%, var(--carrot-body) 40%, var(--carrot-body) 100%); }
  .card--mushroom .card__character { background: linear-gradient(180deg, var(--mushroom-cap) 0%, var(--mushroom-cap) 35%, var(--mushroom-stem) 65%, var(--mushroom-stem) 100%); }

  .card__series {
    position: absolute;
    left: 28px; right: 28px;
    top: 332px;
    height: 38px;
    border-radius: 19px;
    background: var(--pill);
    font-family: "Ubuntu", sans-serif;
    font-weight: 700;
    font-size: 22px;
    line-height: 38px;
    color: var(--pill-text);
  }
  .card__fact {
    position: absolute;
    left: 0; right: 0;
    top: 380px;
    font-family: "Fira Sans", sans-serif;
    font-weight: 600;
    font-size: 23px;
    line-height: 28px;
    color: var(--body-text);
  }
</style>
</head>
<body>
<main class="canvas">
  <article class="card-frame card-frame--potato">
    <div class="card card--potato">
      <div class="card__band"></div>
      <p class="card__vitamin">VITAMIN B</p>
      <h2 class="card__name">POTATOES</h2>
      <div class="card__character" role="img" aria-label="Smiling cartoon potato character with gloves and shoes, hands on hips"></div>
      <p class="card__series">NUTRITION SERIES</p>
      <p class="card__fact">healthy brains and<br>good energy</p>
    </div>
  </article>

  <article class="card-frame card-frame--carrot">
    <div class="card card--carrot">
      <div class="card__band"></div>
      <p class="card__vitamin">VITAMIN A</p>
      <h2 class="card__name">CARROT</h2>
      <div class="card__character" role="img" aria-label="Smiling cartoon carrot character with green leafy top and white gloves"></div>
      <p class="card__series">NUTRITION SERIES</p>
      <p class="card__fact">helps you<br>see at night</p>
    </div>
  </article>

  <article class="card-frame card-frame--mushroom">
    <div class="card card--mushroom">
      <div class="card__band"></div>
      <p class="card__vitamin">VITAMIN D</p>
      <h2 class="card__name">MUSHROOM</h2>
      <div class="card__character" role="img" aria-label="Smiling cartoon mushroom character with brown spotted cap and tan stem"></div>
      <p class="card__series">NUTRITION SERIES</p>
      <p class="card__fact">helps your<br>bones strong</p>
    </div>
  </article>
</main>
</body>
</html>
```